Design Brief for Website Redesign

Client Name: Bluecrest IT
Website: www.bluecrestit.com.au
Industry: Managed IT Services
Target Audience: Small to medium-sized businesses in Australia, requiring IT solutions, IT support, cloud services, and phone systems.

Project Overview
We are seeking a full redesign of the Bluecrest IT website to modernize its look, improve usability, and enhance user experience across devices. The goal is to create a professional, clean, and user-friendly website that reflects our expertise in IT services and appeals to our business clients.

Objectives
Modern Visual Identity: Create a fresh, modern design that aligns with Bluecrest IT's branding.

Improved User Experience: Simplify navigation, improve accessibility, and enhance mobile responsiveness.

Clear Calls to Action: Ensure CTAs are prominent and encourage user engagement.

Enhanced Trust & Credibility: Highlight testimonials, case studies, and industry credentials.

SEO Optimization: Ensure the site is optimized for search engines, including proper heading structures and metadata.
Design Style & Tone
Professional: Clean, modern, and polished to reflect our IT expertise.

Minimalist: Simple layouts, plenty of white space, and easy-to-read typography.

Tech-focused: Subtle tech-themed design elements that reinforce our brand as a leading IT service provider.

Colors: Use our existing brand colors, or propose a color scheme that complements the tech industry while maintaining a professional feel.

Typography: Clear, readable fonts that convey professionalism and trustworthiness.

Key Pages & Features
Home Page:

Hero section with a clear value proposition.

Highlight key services (IT support, cloud solutions, phone systems, etc.) with icons and brief descriptions.

Prominent CTAs (e.g., “Request a Quote,” “Book a Demo”).

Testimonials from satisfied clients.

Services Page:

Detailed breakdown of the services we offer (IT support, cloud services, phone systems, etc.).

Use of icons or illustrations to make the services visually engaging.

Clear CTAs to request quotes or book consultations.

About Us Page:

Information about our company history, mission, and team.

Highlight our certifications, partnerships, and industry expertise.

Case Studies/Testimonials Page:

Showcase client success stories and testimonials with visuals and brief case study summaries.

Include a trust-building section with logos of major clients or partners.

Contact Page:

Simple contact form for inquiries.

Integrated map with office location.

Social media links and phone number.

Blog/Resource Section:

Easy-to-navigate blog section for IT-related articles, tips, and industry news.

Clear categorization and tags for easy browsing.

Knowledge Base/Support Page:

Self-service area for clients to find articles, FAQs, and support guides.

Option to submit a support ticket.

Mobile Responsiveness:

Ensure the design is fully responsive, with no horizontal scrolling or misaligned content on mobile.

Functional Requirements
Fast Load Times: Optimize images, minimize unnecessary scripts, and ensure the site loads quickly on both desktop and mobile.

User-Friendly CMS: We need a CMS that is easy to update (preferably WordPress, but open to other suggestions).

SEO Best Practices: Structure the site with proper metadata, alt tags, and semantic HTML for better search engine optimization.

Security: Ensure the website follows security best practices (SSL, HTTPS).

Deliverables
Full website design (desktop and mobile versions).

Design mockups in Photoshop, Sketch, or Figma (whichever is preferred).

Working prototype (optional).

Final website files, including images and assets.

A style guide for ongoing consistency.

Industry/Entity Type

IT Managed Services

Number of Pages Required

3 page

Requirements
Must have
• EXCELLENT UX/UI

```html
<!DOCTYPE html>
<html lang="en">
<head>
<meta charset="utf-8">
<title>Bluecrest IT — Managed IT Services Sydney</title>
<link href="https://fonts.googleapis.com/css2?family=Righteous&family=Roboto:wght@400;500;700&display=swap" rel="stylesheet">
<style>
:root{
  --red:#e31e3c;
  --ink:#1d1d1f;
  --text:#333;
  --muted:#666;
  --line:#d6d6d6;
  --soft:#f4f4f4;
  --footer:#1f1f21;
  --white:#fff;
  --hero-top:#9a9a9a;
  --hero-bottom:#5e5e5e;
}
*{box-sizing:border-box;margin:0;padding:0}
html,body{width:1200px;height:3395px;overflow:hidden}
body{position:relative;font-family:'Roboto',Arial,sans-serif;color:var(--text);background:var(--white)}
.abs{position:absolute}
.display{font-family:'Righteous',cursive}

/* header */
.site-header{position:absolute;left:0;top:0;width:1200px;height:71px;background:var(--white)}
.brand{left:143px;top:14px;font-family:'Roboto',sans-serif;font-weight:700;font-size:32px;color:var(--red);letter-spacing:-.5px}
.nav{top:26px;font-size:15px;color:#333;text-transform:uppercase}
.nav.active{color:var(--red)}
.nav-underline{left:411px;top:67px;width:46px;height:4px;background:var(--red)}
.btn{display:flex;align-items:center;justify-content:center;gap:8px;border-radius:30px;font-weight:500;text-transform:uppercase;font-size:15px}
.btn-solid{background:var(--red);color:var(--white)}
.btn-outline{border:2px solid var(--red);color:var(--red);background:var(--white)}
.quote-btn{left:914px;top:16px;width:142px;height:36px;font-size:15px}

/* hero */
.hero{left:0;top:71px;width:1200px;height:641px;background:linear-gradient(180deg,var(--hero-top) 0%,#7d7d7d 55%,var(--hero-bottom) 100%)}
.hero-word{left:0;top:220px;width:1200px;text-align:center;font-family:'Roboto',sans-serif;font-weight:700;font-size:210px;line-height:1;color:var(--red);letter-spacing:-6px}

/* sections */
.squiggle{width:96px;height:12px}
.section-title{width:1200px;left:0;text-align:center;font-size:60px;color:var(--ink);line-height:1}

/* services */
.card{border:1.5px solid var(--line);border-radius:14px;background:var(--white);width:286px;height:368px;top:899px}
.card.featured{border:2.5px solid var(--red)}
.card .icon{position:absolute;left:82px;top:28px;width:122px;height:122px;border-radius:50%;border:3px solid #ddd;background:var(--white)}
.card .icon span{position:absolute;left:6px;top:6px;width:104px;height:104px;border-radius:50%;background:var(--red);display:flex;align-items:center;justify-content:center}
.card h3{position:absolute;left:0;top:170px;width:100%;text-align:center;font-size:20px;font-weight:500;color:var(--ink)}
.card p{position:absolute;left:30px;top:207px;width:224px;text-align:center;font-size:14px;line-height:20px;color:#333}
.card .go{position:absolute;left:123px;top:298px;width:40px;height:40px;border-radius:50%;background:#e4e4e4;display:flex;align-items:center;justify-content:center}
.card.featured .go{background:var(--red)}

/* about */
.about-photo{left:0;top:1345px;width:603px;height:501px}
.about-title{left:643px;top:1457px;font-size:60px;color:var(--ink);line-height:1}
.about-text{left:645px;top:1537px;width:415px;font-size:14.5px;line-height:21.6px;color:#333}
.learn-btn{left:643px;top:1731px;width:206px;height:54px}

/* testimonials */
.testimonials{left:0;top:1846px;width:1200px;height:667px;background:var(--soft)}
.t-card{top:2085px;width:286px;height:267px;background:var(--white);border-radius:8px;border-top:7px solid #999;box-shadow:0 8px 18px rgba(0,0,0,.07)}
.t-card.featured{border-top-color:var(--red)}
.avatar{position:absolute;left:101px;top:-35px;width:86px;height:86px;border-radius:50%;border:3px solid var(--white)}
.stars{position:absolute;left:0;top:72px;width:100%;text-align:center;color:#f6b100;font-size:17px;letter-spacing:6px}
.t-card p{position:absolute;left:24px;top:100px;width:238px;text-align:center;font-size:12.5px;line-height:20.7px;color:#666}
.t-name{position:absolute;left:0;top:186px;width:100%;text-align:center;font-size:20px;font-weight:500;color:#444}
.t-time{position:absolute;left:0;top:215px;width:100%;text-align:center;font-size:15px;color:#555}
.dot{top:2393px;width:14px;height:14px;border-radius:50%;background:#d9d9d9}

/* contact cta */
.cta-sub{left:0;width:1200px;text-align:center;font-size:18px;color:var(--ink)}
.cta-text{left:235px;top:2778px;width:730px;text-align:center;font-size:14.5px;line-height:21.6px;color:#333}

/* footer */
.site-footer{left:0;top:3004px;width:1200px;height:391px;background:linear-gradient(135deg,#242426,#1a1a1b)}
.f-head{color:var(--white);font-size:21px;font-weight:500;line-height:28px;text-transform:uppercase}
.f-input{left:143px;top:3150px;width:272px;height:42px;border:1px solid #888;display:flex;align-items:center;padding:0 12px;font-size:12px;color:#ddd;justify-content:space-between}
.social{top:3216px;width:22px;height:22px;border-radius:50%;background:#444}
.social.on{background:var(--white);width:28px;height:28px;top:3213px}
.ci{left:502px;color:var(--white)}
.ci b{display:block;font-size:15px;font-weight:700}
.ci small{display:block;font-size:12px;color:#ddd;margin-top:6px}
.ql{font-size:15px;color:var(--white);display:flex;align-items:center;gap:10px;font-weight:500}
.ql i{color:var(--red);font-style:normal;font-size:13px}
.f-rule{left:0;top:3317px;width:1200px;height:1px;background:#333}
.copy{left:0;top:3347px;width:1200px;text-align:center;font-size:15px;color:#ddd}
</style>
</head>
<body>

<header class="site-header">
  <div class="abs brand">Bluecrest</div>
  <div class="abs nav active" style="left:411px">Home</div>
  <div class="abs nav" style="left:483px">Services</div>
  <div class="abs nav" style="left:582px">About</div>
  <div class="abs nav" style="left:659px">Contact</div>
  <div class="abs nav" style="left:756px">Support</div>
  <div class="abs nav-underline"></div>
  <div class="abs btn btn-solid quote-btn">Get a Quote</div>
</header>

<section class="abs hero" role="img" aria-label="Photo of the Bluecrest IT team standing together in the office">
</section>
<div class="abs hero-word" aria-hidden="true">Bluecrest</div>

<!-- services -->
<svg class="abs squiggle" style="left:552px;top:781px" viewBox="0 0 96 12"><path d="M2 3l6 6 6-6 6 6 6-6 6 6 6-6 6 6 6-6 6 6 6-6 6 6 6-6 6 6 6-6 6 6" fill="none" stroke="var(--red)" stroke-width="2.4"/></svg>
<h2 class="abs section-title display" style="top:810px">Our Services</h2>

<svg class="abs" style="left:64px;top:1062px" width="20" height="26" viewBox="0 0 20 26"><path d="M15 3L5 13l10 10" fill="none" stroke="#222" stroke-width="3"/></svg>
<svg class="abs" style="left:1116px;top:1062px" width="20" height="26" viewBox="0 0 20 26"><path d="M5 3l10 10-10 10" fill="none" stroke="#222" stroke-width="3"/></svg>

<article class="abs card" style="left:144px">
  <div class="icon"><span><svg width="56" height="56" viewBox="0 0 56 56" fill="none" stroke="#fff" stroke-width="2.2"><circle cx="24" cy="16" r="8"/><path d="M10 44c0-9 6-15 14-15s14 6 14 15z"/><rect x="10" y="44" width="28" height="4"/><circle cx="40" cy="30" r="7"/><path d="M37 33l6-6"/></svg></span></div>
  <h3>IT Support</h3>
  <p>Lorem ipsum dolor sit amet, con sectetur adipiscing elit, sed do eiusmod tempor incididunt ut dolore magna aliqua.</p>
  <div class="go"><svg width="10" height="12" viewBox="0 0 10 12"><path d="M3 1l5 5-5 5" fill="none" stroke="#333" stroke-width="1.6"/></svg></div>
</article>
<article class="abs card featured" style="left:456px">
  <div class="icon" style="left:80px"><span><svg width="58" height="58" viewBox="0 0 58 58" fill="none" stroke="#fff" stroke-width="2.2"><path d="M14 46a9 9 0 0 1 1-18 13 13 0 0 1 26-2 10 10 0 0 1 3 20z"/><circle cx="29" cy="22" r="6"/><path d="M29 28v8M29 6v5M18 11l3 3M40 11l-3 3"/><path d="M34 38l4 4 7-7"/></svg></span></div>
  <h3>Cloud Solutions</h3>
  <p>Lorem ipsum dolor sit amet, con sectetur adipiscing elit, sed do eiusmod tempor incididunt ut dolore magna aliqua.</p>
  <div class="go" style="left:121px"><svg width="10" height="12" viewBox="0 0 10 12"><path d="M3 1l5 5-5 5" fill="none" stroke="#fff" stroke-width="1.8"/></svg></div>
</article>
<article class="abs card" style="left:770px">
  <div class="icon"><span><svg width="56" height="56" viewBox="0 0 56 56" fill="none" stroke="#fff" stroke-width="2.2"><rect x="16" y="6" width="24" height="42" rx="4"/><path d="M24 10h8M26 43h4"/><circle cx="28" cy="24" r="6"/><path d="M30 34l12 12M42 34L32 44"/></svg></span></div>
  <h3>Phone Systems</h3>
  <p>Lorem ipsum dolor sit amet, con sectetur adipiscing elit, sed do eiusmod tempor incididunt ut dolore magna aliqua.</p>
  <div class="go"><svg width="10" height="12" viewBox="0 0 10 12"><path d="M3 1l5 5-5 5" fill="none" stroke="#333" stroke-width="1.6"/></svg></div>
</article>

<!-- about -->
<svg class="abs about-photo" viewBox="0 0 603 501" role="img" aria-label="Colleagues in a bright office reviewing work on a tablet">
  <defs><linearGradient id="aboutTone" x1="0" y1="0" x2="1" y2="1"><stop offset="0" stop-color="#6d737a"/><stop offset=".5" stop-color="#a6a9ad"/><stop offset="1" stop-color="#3f4a5c"/></linearGradient></defs>
  <path d="M0 30H390a210 210 0 0 1 210 210v10A250 250 0 0 1 350 501H0z" fill="url(#aboutTone)"/>
  <path d="M0 32H390a208 208 0 0 1 208 208" fill="none" stroke="var(--red)" stroke-width="10"/>
</svg>
<svg class="abs squiggle" style="left:643px;top:1429px" viewBox="0 0 96 12"><path d="M2 3l6 6 6-6 6 6 6-6 6 6 6-6 6 6 6-6 6 6 6-6 6 6 6-6 6 6 6-6 6 6" fill="none" stroke="var(--red)" stroke-width="2.4"/></svg>
<h2 class="abs about-title display">About Us</h2>
<p class="abs about-text">Founded in 1997 in Sydney, Bluecrest IT began as a dedicated IT managed services provider, delivering reliable technology solutions to local businesses. Since then, our expertise, services, and support have evolved significantly, transforming us into a leading End-to-End IT Solutions provider for Small &amp; Medium Businesses. Today, we proudly support offices across Australia, helping businesses streamline operations, enhance security, and embrace innovation.</p>
<div class="abs btn btn-solid learn-btn">Learn More <svg width="9" height="12" viewBox="0 0 9 12"><path d="M2 1l5 5-5 5" fill="none" stroke="#fff" stroke-width="2.2"/></svg></div>

<!-- testimonials -->
<section class="abs testimonials"></section>
<svg class="abs squiggle" style="left:552px;top:1934px" viewBox="0 0 96 12"><path d="M2 3l6 6 6-6 6 6 6-6 6 6 6-6 6 6 6-6 6 6 6-6 6 6 6-6 6 6 6-6 6 6" fill="none" stroke="var(--red)" stroke-width="2.4"/></svg>
<h2 class="abs section-title display" style="top:1962px">Testimonials</h2>

<article class="abs t-card" style="left:144px">
  <div class="avatar" role="img" aria-label="Client portrait" style="background:linear-gradient(#b9a08a,#6e5b4c)"></div>
  <div class="stars">★★★★★</div>
  <p>Lorem ipsum dolor sit amet, consectetur adipiscing elit, sed do eiusmod tempor incididunt ut labore et dolore magna ad minim veniam</p>
  <div class="t-name">Mara Ellison.</div>
  <div class="t-time">4 month ago</div>
</article>
<article class="abs t-card featured" style="left:456px">
  <div class="avatar" role="img" aria-label="Client portrait" style="background:linear-gradient(#c9c9c9,#6b6b6b)"></div>
  <div class="stars">★★★★★</div>
  <p>Lorem ipsum dolor sit amet, consectetur adipiscing elit, sed do eiusmod tempor incididunt ut labore et dolore magna ad minim veniam</p>
  <div class="t-name">Tessa K.</div>
  <div class="t-time">6 month ago</div>
  <div style="position:absolute;left:222px;top:240px;width:40px;height:40px;border-radius:50%;background:#fff;color:var(--red);font-family:'Righteous',cursive;font-size:44px;line-height:52px;text-align:center">“</div>
</article>
<article class="abs t-card" style="left:770px">
  <div class="avatar" role="img" aria-label="Client portrait" style="background:linear-gradient(#8fc3e6,#3c6f96)"></div>
  <div class="stars" style="top:64px">★★★★★</div>
  <p style="top:92px">Lorem ipsum dolor sit amet, consectetur adipiscing elit, sed do eiusmod tempor incididunt ut labore et dolore magna ad minim veniam</p>
  <div class="t-name">Dev Narang</div>
  <div class="t-time">6 month ago</div>
</article>
<div class="abs dot" style="left:569px"></div>
<div class="abs dot" style="left:593px;background:var(--red)"></div>
<div class="abs dot" style="left:617px"></div>

<!-- contact cta -->
<svg class="abs squiggle" style="left:552px;top:2598px" viewBox="0 0 96 12"><path d="M2 3l6 6 6-6 6 6 6-6 6 6 6-6 6 6 6-6 6 6 6-6 6 6 6-6 6 6 6-6 6 6" fill="none" stroke="var(--red)" stroke-width="2.4"/></svg>
<h2 class="abs section-title display" style="top:2627px">Let’s Get In Touch</h2>
<div class="abs cta-sub" style="top:2711px">Looking for IT Support in Sydney?</div>
<div class="abs cta-sub" style="top:2739px">Explore Managed IT Support Services for Your Business</div>
<p class="abs cta-text">Get help managing IT for your small or medium business from our team based right here in Sydney. Whether your team is working on-site or remotely, Bluecrest IT can help you streamline your operations. Contact us today to schedule a consultation and learn how we can support your business goals.</p>
<div class="abs btn btn-solid" style="left:372px;top:2860px;width:221px;height:53px">Request a Quote <svg width="9" height="12" viewBox="0 0 9 12"><path d="M2 1l5 5-5 5" fill="none" stroke="#fff" stroke-width="2.2"/></svg></div>
<div class="abs btn btn-outline" style="left:605px;top:2860px;width:222px;height:53px;font-weight:400">Book a Demo <svg width="9" height="12" viewBox="0 0 9 12"><path d="M2 1l5 5-5 5" fill="none" stroke="var(--red)" stroke-width="2.2"/></svg></div>

<!-- footer -->
<footer class="abs site-footer"></footer>
<div class="abs f-head" style="left:143px;top:3080px">Subscribe to<br>our newsletter</div>
<div class="abs f-input">Email address <svg width="14" height="14" viewBox="0 0 14 14"><path d="M1 7L13 1 9 13 7 8z" fill="var(--red)"/></svg></div>
<div class="abs social" style="left:148px" aria-label="Social link"></div>
<div class="abs social on" style="left:177px" aria-label="Social link"></div>
<div class="abs social" style="left:212px" aria-label="Social link"></div>

<div class="abs f-head" style="left:502px;top:3082px">Contact Info</div>
<svg class="abs" style="left:503px;top:3136px" width="14" height="20" viewBox="0 0 14 20"><path d="M7 19S1 11 1 7a6 6 0 0 1 12 0c0 4-6 12-6 12z" fill="none" stroke="var(--red)" stroke-width="2"/><circle cx="7" cy="7" r="2" fill="var(--red)"/></svg>
<div class="abs ci" style="left:546px;top:3138px"><b>Address</b><small>Sydney, Australia</small></div>
<svg class="abs" style="left:503px;top:3197px" width="20" height="14" viewBox="0 0 20 14"><rect width="20" height="14" rx="1" fill="var(--red)"/><path d="M1 1l9 7 9-7" fill="none" stroke="#222" stroke-width="1.5"/></svg>
<div class="abs ci" style="left:546px;top:3194px"><b>Email</b><small>info@bluecrestit.com.au</small></div>
<svg class="abs" style="left:503px;top:3252px" width="18" height="18" viewBox="0 0 18 18"><path d="M4 1l3 4-2 2c1 3 3 5 6 6l2-2 4 3-2 3C7 17 1 11 1 3z" fill="var(--red)"/></svg>
<div class="abs ci" style="left:546px;top:3250px"><b>Phone</b><small>1300 555 014</small></div>

<div class="abs f-head" style="left:765px;top:3082px">Quick Links</div>
<div class="abs ql" style="left:765px;top:3136px"><i>»</i>Home</div>
<div class="abs ql" style="left:765px;top:3168px"><i>»</i>About</div>
<div class="abs ql" style="left:765px;top:3200px"><i>»</i>Services</div>
<div class="abs ql" style="left:765px;top:3232px"><i>»</i>Contact</div>
<div class="abs ql" style="left:900px;top:3136px"><i>»</i>Terms and Condition</div>
<div class="abs ql" style="left:900px;top:3168px"><i>»</i>Privacy policy</div>
<div class="abs ql" style="left:900px;top:3200px"><i>»</i>Help</div>
<div class="abs ql" style="left:900px;top:3232px"><i>»</i>Support</div>

<div class="abs f-rule"></div>
<div class="abs copy">© Copyrights 2025 | All Rights Reserved</div>

</body>
</html>
```